Website for Party

Design a new website for PrismGatherings.com
We have attached the new logos and please look at the website, and our facebook page: facebook.com/prismgatherings for inspiration
Updates

Hi Guys, please be original with all designs and images otherwise the design will be eliminated Thank you

some of your designs have too much happening in them, others make it clear that the designer has not yet read the brief fully

Please everyone be original!

```html
<!DOCTYPE html>
<html lang="en">
<head>
<meta charset="utf-8">
<title>Prism Gatherings</title>
<link href="https://fonts.googleapis.com/css2?family=Inter:wght@300;400;500&family=Open+Sans:wght@400&display=swap" rel="stylesheet">
<style>
  :root {
    --ink: #000000;
    --panel: #0e0e0e;
    --white: #ffffff;
    --nav-text: #2a2a2a;
    --muted: #d8d8d8;
    --rule: #3a3a3a;
    --hero-light: #cfc6bb;
    --hero-mid: #9a8a7a;
    --hero-dark: #4a3e36;
  }
  * { margin: 0; padding: 0; box-sizing: border-box; }
  html, body { width: 1167px; height: 1200px; overflow: hidden; background: var(--ink); }
  body { position: relative; font-family: "Open Sans", sans-serif; }

  .hero {
    position: absolute; left: 0; top: 0; width: 1167px; height: 602px;
    background:
      radial-gradient(ellipse 60% 45% at 52% 18%, var(--hero-light) 0%, rgba(207,198,187,0) 70%),
      linear-gradient(180deg, #bdb2a6 0%, var(--hero-mid) 45%, var(--hero-dark) 100%);
  }
  .brand-box {
    position: absolute; left: 126px; top: 0; width: 166px; height: 143px;
    background: var(--ink); display: flex; align-items: center; justify-content: center;
  }
  .brand-name {
    color: var(--white); font-family: "Inter", sans-serif; font-weight: 500;
    font-size: 26px; letter-spacing: 2px;
  }
  .main-nav {
    position: absolute; top: 18px; left: 378px; display: flex;
    font-family: "Inter", sans-serif; font-size: 18px; color: var(--nav-text);
  }
  .main-nav span { margin-right: 39px; }
  .social {
    position: absolute; left: 902px; top: 16px; display: flex; gap: 5px;
  }
  .social i { width: 24px; height: 24px; border-radius: 50%; background: #3b3632; display: block; }

  .hero-mark {
    position: absolute; left: 0; width: 100%; top: 150px; text-align: center;
    font-family: "Inter", sans-serif; font-weight: 500; font-size: 54px;
    color: rgba(120,105,92,0.35);
  }
  .hero-title {
    position: absolute; left: 0; width: 100%; top: 236px; text-align: center;
    font-family: "Inter", sans-serif; font-weight: 300; font-size: 67px;
    letter-spacing: -2px; color: var(--ink);
  }
  .hero-text {
    position: absolute; left: 250px; width: 667px; top: 318px; text-align: center;
    font-family: "Inter", sans-serif; font-weight: 300; font-size: 16.5px; line-height: 21px;
    color: var(--white);
  }
  .learn-more {
    position: absolute; left: 507px; top: 381px; width: 153px; height: 51px;
    background: linear-gradient(180deg, #3a3a3a 0%, #0d0d0d 100%); border-radius: 3px;
    color: var(--white); font-family: "Inter", sans-serif; font-size: 17px;
    display: flex; align-items: center; justify-content: center;
  }
  .slide-dots { position: absolute; left: 553px; top: 495px; display: flex; gap: 4px; }
  .slide-dots i { width: 17px; height: 17px; border-radius: 50%; background: var(--white); display: block; }
  .slide-dots i.active { background: var(--ink); }

  .features { position: absolute; left: 0; top: 602px; width: 1167px; height: 456px; background: var(--ink); }
  .photo { position: absolute; }
  .photo-cruise { left: 125px; top: 0; width: 305px; height: 216px;
    background: linear-gradient(180deg, #6b78c8 0%, #8a7fc0 45%, #2f3c7a 70%, #1c2250 100%); }
  .photo-food { left: 430px; top: 222px; width: 243px; height: 216px;
    background: radial-gradient(ellipse at 55% 50%, #d9a46a 0%, #b5a27a 35%, #9fb7bf 75%, #c8d6da 100%); }
  .photo-bar { left: 676px; top: 0; width: 366px; height: 216px;
    background: linear-gradient(90deg, #2a2a2a 0%, #4a4a4a 30%, #1d2a4a 65%, #141b30 100%); }

  .card { position: absolute; background: var(--panel); color: var(--white); }
  .card h2 { font-family: "Inter", sans-serif; font-weight: 400; font-size: 20px; line-height: 21px; letter-spacing: 0.5px; }
  .card p { font-size: 12.3px; line-height: 19px; color: var(--muted); }
  .card-cruise { left: 125px; top: 216px; width: 305px; height: 222px; padding: 38px 20px 0 15px; }
  .card-cruise p { margin-top: 20px; }
  .card-hors { left: 430px; top: 0; width: 243px; height: 222px; background: var(--ink); padding: 24px 20px 0 25px; }
  .card-hors p { margin-top: 16px; }
  .card-bar { left: 673px; top: 216px; width: 369px; height: 222px; padding: 38px 20px 0 17px; }
  .card-bar p { margin-top: 20px; }
  .pointer { position: absolute; }

  .slider-arrow { position: absolute; top: 208px; }

  .site-footer { position: absolute; left: 0; top: 1058px; width: 1167px; height: 142px; background: #050505; border-top: 1px solid var(--rule); }
  .footer-links { position: absolute; left: 126px; top: topleft; font-size: 11.5px; color: var(--white); }
  .footer-links { top: 55px; }
  .footer-links span + span { margin-left: 18px; }
  .footer-links .dot { margin-left: 18px; }
  .copyright { position: absolute; left: 125px; top: 79px; font-size: 11.5px; color: var(--white); }
  .partner-badge { position: absolute; left: 944px; top: 17px; width: 97px; height: 97px; background: var(--white); }
</style>
</head>
<body>
  <header class="hero">
    <div role="img" aria-label="Concert crowd with raised hands under stage haze" style="position:absolute;inset:0;"></div>
    <div class="brand-box"><span class="brand-name">Prism</span></div>
    <nav class="main-nav">
      <span>Welcome</span><span>About</span><span>FAQ</span><span>Order Tickets</span><span>Contact</span>
    </nav>
    <div class="social" aria-label="Social links"><i></i><i></i><i></i><i></i><i></i></div>
    <div class="hero-mark">Prism</div>
    <h1 class="hero-title">Prism Gatherings</h1>
    <p class="hero-text">Consuetudium lectorum. Mirum est notare quam littera gothica, quam nunc putamus parum claram, anteposuerit litterarum formas humanitatis pa et quinta decima.</p>
    <div class="learn-more">Learn More</div>
    <div class="slide-dots"><i class="active"></i><i></i><i></i></div>
  </header>

  <section class="features">
    <div class="photo photo-cruise" role="img" aria-label="Lit yacht cruising the harbor beneath a bridge at dusk"></div>
    <div class="photo photo-food" role="img" aria-label="Plated seafood hors d'oeuvres in pastry shells"></div>
    <div class="photo photo-bar" role="img" aria-label="Bartender pouring a cocktail into a martini glass"></div>

    <div class="card card-cruise">
      <h2>3+ Hour Cruise<br>around NYC Harbor</h2>
      <p>Over 3 hours of cruising through the NYC harbor. Enjoy the open-air deck and admire magnificent views of Manhattan's stunning skyline at sunset with your sweetheart.</p>
    </div>
    <div class="card card-hors">
      <h2>Hors d'oeuvres</h2>
      <p>Enjoy light refreshments while waiting to board the yacht. Hand-baked by refreshments created by our executive chef and served by our own private waiters.</p>
    </div>
    <div class="card card-bar">
      <h2>Open Premium Bar</h2>
      <p>Enjoy your choice of beer, whiskey, tequila, vodka, and wine, or have one of our professional bartenders prepare your favorite mixed drink.&nbsp; Attend our private lounge with a delicious cocktail and watch the stunning view of Manhattan's skyline.</p>
    </div>

    <svg class="pointer" style="left:250px;top:200px" width="38" height="17"><polygon points="0,17 19,0 38,17" fill="#0e0e0e"/></svg>
    <svg class="pointer" style="left:520px;top:222px" width="44" height="17"><polygon points="0,0 44,0 22,17" fill="#000"/></svg>
    <svg class="pointer" style="left:841px;top:199px" width="42" height="18"><polygon points="0,18 21,0 42,18" fill="#0e0e0e"/></svg>

    <svg class="slider-arrow" style="left:80px" width="16" height="30"><polyline points="15,1 2,15 15,29" fill="none" stroke="#fff" stroke-width="1.2"/></svg>
    <svg class="slider-arrow" style="left:1071px" width="16" height="30"><polyline points="1,1 14,15 1,29" fill="none" stroke="#fff" stroke-width="1.2"/></svg>
  </section>

  <footer class="site-footer">
    <div class="footer-links"><span>Privacy Policy</span><span class="dot">.</span><span>Terms &amp; Conditions</span></div>
    <div class="copyright">© 2014&nbsp; PrismGatherings.com All rights reserved</div>
    <div class="partner-badge" aria-label="Partner event badge"></div>
  </footer>
</body>
</html>
```